Business card design incorporating discount offer

We are a trade services company and we need a double sided business card that is going to be used by our tradesmen to give to customers on completion of their jobs.

Below are the key elements of the card that we would like to include:

-Main logo with text 'Expert Property Care' underneath.
-Up to 12 smaller icon logos with text 'Your local all-trade experts' to emphasise the point that we cover all the trades
-Discount offer - 10% discount
-Telephone number and website address
-Blank space for tradesman to enter his/her name
-Request for customer feedback with feedback url

This business card will be printed on regular card. In the past we have favoured designs that use a black background but we're open to new ideas.

I have attached a few files:

-A simple wire frame example to show how this card could look with the different elements mentioned above, feel free to use a layout similar to this or come up with something totally different (biz-card.pdf)
-Front and back of a loyalty card the we've used in the past (this card was printed on plastic)
-Front and back of a key fob design that we've previously used (this card was printed on plastic)
-A logo file with the 12 small icons and the main logo image

If you need further images or information please ask.

```html
<!DOCTYPE html>
<html lang="en">
<head>
<meta charset="utf-8">
<title>RTK Business Card</title>
<link rel="stylesheet" href="https://fonts.googleapis.com/css2?family=Montserrat:wght@500;600;700;800&display=swap">
<style>
  :root {
    --ink: #000000;
    --paper: #ffffff;
    --brand-blue: #0a7cc4;
    --tile-dark: #3a3a3a;
    --tile-light: #8a8a8a;
    --shadow: rgba(0,0,0,0.45);
  }
  * { box-sizing: border-box; margin: 0; padding: 0; }
  html, body { width: 1200px; height: 1000px; overflow: hidden; background: var(--paper); }
  body { position: relative; font-family: "Montserrat", sans-serif; }

  .card { position: absolute; overflow: hidden; box-shadow: 6px 8px 14px var(--shadow); }
  .card--front { left: 261px; top: 44px; width: 692px; height: 434px; background: var(--ink); }
  .card--back { left: 259px; top: 521px; width: 694px; height: 436px; background: var(--ink); }

  .abs { position: absolute; }

  /* front */
  .brand-name { left: 0; width: 477px; top: 100px; text-align: center; color: var(--paper);
    font-weight: 700; font-size: 88px; letter-spacing: 2px; line-height: 1; }
  .tagline { left: 0; width: 477px; top: 220px; text-align: center; color: var(--paper);
    font-weight: 600; font-size: 35px; }
  .contact-row { left: 36px; display: flex; align-items: center; gap: 10px; color: var(--paper); font-weight: 600; }
  .contact-row--phone { top: 314px; font-size: 41px; }
  .contact-row--web { top: 370px; font-size: 29px; }
  .contact-row svg { width: 42px; height: 42px; flex: none; }

  .offer-panel { left: 477px; top: 0; width: 215px; height: 434px; background: var(--paper);
    color: var(--ink); text-align: center; }
  .offer-value { position: absolute; left: 0; width: 215px; top: 88px; color: var(--brand-blue);
    font-weight: 700; font-size: 100px; line-height: 1; letter-spacing: -3px; }
  .offer-value sup { font-size: 26px; vertical-align: top; position: relative; top: 6px; letter-spacing: 0; }
  .offer-title { position: absolute; left: 0; width: 215px; top: 182px; font-weight: 800; font-size: 25px; }
  .offer-note { position: absolute; left: 0; width: 215px; top: 214px; font-weight: 700; font-size: 12.5px; }
  .offer-link { position: absolute; left: 0; width: 215px; top: 316px; font-weight: 800; line-height: 1.05; }
  .offer-link .small { font-size: 14.5px; display: block; }
  .offer-link .big { font-size: 27px; color: var(--brand-blue); display: block; }

  /* back */
  .trades-panel { left: 0; top: 0; width: 216px; height: 436px; background: var(--paper); }
  .trade-tile { position: absolute; width: 72px; height: 72px; border-radius: 12px;
    border: 3px solid #222; background: linear-gradient(180deg, var(--tile-light) 0%, #6a6a6a 48%, var(--tile-dark) 52%, #2a2a2a 100%); }
  .headline { left: 216px; width: 478px; top: 27px; text-align: center; color: var(--paper); font-weight: 600; font-size: 24px; }
  .tradesman-label { left: 216px; width: 478px; top: 155px; text-align: center; color: var(--brand-blue); font-weight: 600; font-size: 16px; }
  .tradesman-field { left: 288px; top: 182px; width: 336px; height: 39px; background: var(--paper); }
  .feedback-question { left: 216px; width: 478px; top: 323px; text-align: center; color: var(--paper); font-weight: 500; font-size: 19px; }
  .feedback-prompt { left: 216px; width: 478px; top: 359px; text-align: center; color: var(--brand-blue); font-weight: 500; font-size: 16.5px; }
  .feedback-url { left: 216px; width: 478px; top: 382px; text-align: center; color: var(--paper); font-weight: 500; font-size: 22px; }
</style>
</head>
<body>

<section class="card card--front">
  <div class="abs brand-name">RTK</div>
  <div class="abs tagline">Expert Property Care</div>

  <div class="abs contact-row contact-row--phone">
    <svg viewBox="0 0 42 42" aria-hidden="true">
      <circle cx="21" cy="21" r="19" fill="none" stroke="var(--brand-blue)" stroke-width="2.5"/>
      <path d="M14 11c2-1 3 0 4 3s0 4-1 5c1 3 3 5 6 6 1-1 2-2 5-1s4 2 3 4c-1 2-3 3-6 2-6-2-11-7-13-13-1-3 0-5 2-6z" fill="var(--brand-blue)"/>
    </svg>
    <span>0800 000 4821</span>
  </div>
  <div class="abs contact-row contact-row--web">
    <svg viewBox="0 0 42 42" aria-hidden="true" fill="none" stroke="var(--brand-blue)" stroke-width="2">
      <circle cx="21" cy="21" r="18"/>
      <ellipse cx="21" cy="21" rx="8" ry="18"/>
      <line x1="21" y1="3" x2="21" y2="39"/>
      <line x1="3" y1="21" x2="39" y2="21"/>
      <path d="M6 12h30M6 30h30"/>
    </svg>
    <span>RTK-SERVICES.CO.UK</span>
  </div>

  <div class="abs offer-panel">
    <div class="offer-value">10<sup>%</sup></div>
    <div class="offer-title">DISCOUNT</div>
    <div class="offer-note">WITH THIS CARD</div>
    <div class="offer-link">
      <span class="small">CHECK OUT OUR</span>
      <span class="big">WEBSITE</span>
      <span class="small">FOR FULL OFFER</span>
      <span class="big">DETAILS</span>
    </div>
  </div>
</section>

<section class="card card--back">
  <div class="abs trades-panel">
    <div class="trade-tile" style="left:27px;top:19px" role="img" aria-label="Trade icon: water drop"></div>
    <div class="trade-tile" style="left:119px;top:19px" role="img" aria-label="Trade icon: bathtub"></div>
    <div class="trade-tile" style="left:27px;top:101px" role="img" aria-label="Trade icon: oven"></div>
    <div class="trade-tile" style="left:119px;top:101px" role="img" aria-label="Trade icon: pipework"></div>
    <div class="trade-tile" style="left:27px;top:183px" role="img" aria-label="Trade icon: hand saw"></div>
    <div class="trade-tile" style="left:119px;top:183px" role="img" aria-label="Trade icon: gas flame"></div>
    <div class="trade-tile" style="left:27px;top:265px" role="img" aria-label="Trade icon: hammer"></div>
    <div class="trade-tile" style="left:119px;top:265px" role="img" aria-label="Trade icon: paint brush"></div>
    <div class="trade-tile" style="left:27px;top:347px" role="img" aria-label="Trade icon: saw blade and spanner"></div>
    <div class="trade-tile" style="left:119px;top:347px" role="img" aria-label="Trade icon: electricity bolt"></div>
  </div>

  <div class="abs headline">Your Local All-Trade Experts</div>
  <div class="abs tradesman-label">Your RTK Tradesman:</div>
  <div class="abs tradesman-field"></div>
  <div class="abs feedback-question">What do you think of our service?</div>
  <div class="abs feedback-prompt">Please leave feedback online:</div>
  <div class="abs feedback-url">RTK-SERVICES.CO.UK/FEEDBACK</div>
</section>

</body>
</html>
```